Silver Heron Coffee Bean Labels

We need a label for a new brand of coffee that we are selling in Portland, Oregon (Coffee Capital). Our company has no current online presence but have some great roasting techniques. We will be roasting our own coffee beans from throughout the world and selling them immediately after roasting causing a super fresh and high quality product.

We will be packaging in brown kraft bags: 3 3/8 X 2.5 x 7.75 inches which is standard for coffee beans.

Also notice on that sample the blue section in the middle has the product name. We want to also make it so that there is a consistent area that we can print OVER the label the name or blend of the coffee.

Our company is called Silver Heron Coffee Roasters. We will want to put silverheronroasters.example on the label someplace (we dont have a site yet but will by launch).

We need to incorporate A Silver Heron into the design. No preferences yet on the style of it.

We want to be a super-premium brand. Sort of like MicroBrew beers. We will sell at Farmers Markets, online, and directly into stores. Image is very important to us.

Labels should be about 3" wide and about 3.75" high.. Perhaps higher if a cool design justifies the height. Again we will be using a brown kraft bag (like grocery bag color) as shown on the sample.

SEE ATTACHED SEVERAL INTERESTING DESIGNS

Target Market(s)

Foodies, Yuppie, Coffee Snob

Industry/Entity Type

It Company

Requirements
Must have
• Location for the product Name to go onto it... We want to use the same labels for our full line. Just printing over it something like "Italian Roast" and a line below saying something like "Bold, Nutty Flavor, blah blah"

Should not have
• Clunkey looking old fonts or things that look homemade.

```html
<!DOCTYPE html>
<html lang="en">
<head>
<meta charset="utf-8">
<title>Silver Heron Coffee Roasters – Label Options</title>
<link rel="stylesheet" href="https://fonts.googleapis.com/css2?family=Anton&family=Oswald:wght@500;700&family=Open+Sans:wght@600&display=swap">
<style>
  :root {
    --page: #ffffff;
    --label-black: #000000;
    --silver-white: #f2f2f2;
    --pure-white: #ffffff;
    --roast-orange: #ff6a00;
    --blend-yellow: #ffe600;
    --blend-magenta: #ff40ff;
    --kraft-light: #cfae8c;
    --kraft-dark: #5a3b22;
  }
  html, body {
    margin: 0;
    padding: 0;
    width: 1200px;
    height: 900px;
    overflow: hidden;
    background: var(--page);
  }
  .canvas {
    position: relative;
    width: 1200px;
    height: 900px;
  }
  .label {
    position: absolute;
    width: 508px;
    height: 581px;
  }
  .label--cup { left: 84px; top: 182px; }
  .label--gem { left: 647px; top: 187px; }

  .label__bg { fill: var(--label-black); }
  .brand-vertical {
    font-family: "Anton", "Impact", sans-serif;
    fill: var(--silver-white);
  }
  .brand-name {
    font-family: "Anton", "Impact", sans-serif;
    fill: var(--pure-white);
  }
  .brand-tagline {
    font-family: "Oswald", "Arial Narrow", sans-serif;
    font-weight: 700;
    fill: var(--roast-orange);
  }
  .brand-tagline--heavy {
    font-family: "Anton", "Impact", sans-serif;
    font-weight: 400;
  }
  .blend-name {
    font-family: "Oswald", "Arial Narrow", sans-serif;
    font-weight: 500;
  }
  .blend-name--yellow { fill: var(--blend-yellow); }
  .blend-name--magenta { fill: var(--blend-magenta); }
  .overprint-area--yellow { fill: var(--blend-yellow); }
  .overprint-area--magenta { fill: var(--blend-magenta); }
  .web-address {
    font-family: "Open Sans", "Arial", sans-serif;
    font-weight: 600;
    fill: var(--pure-white);
  }
  .kraft-start { stop-color: var(--kraft-light); }
  .kraft-end { stop-color: var(--kraft-dark); }
</style>
</head>
<body>
<main class="canvas">

  <!-- Label option one: cup artwork -->
  <svg class="label label--cup" viewBox="0 0 508 581" aria-label="Silver Heron Coffee Roasters label, Italian Roast">
    <defs>
      <linearGradient id="kraft-cup" x1="1" y1="0" x2="0" y2="1">
        <stop offset="0" class="kraft-end"/>
        <stop offset="0.35" class="kraft-start"/>
        <stop offset="1" class="kraft-end"/>
      </linearGradient>
    </defs>
    <rect class="label__bg" width="508" height="581"/>
    <text class="brand-vertical" transform="translate(172 484) rotate(-90)" font-size="180" textLength="451" lengthAdjust="spacingAndGlyphs">SILVER</text>
    <text class="brand-name" x="192" y="123" font-size="124" textLength="280" lengthAdjust="spacingAndGlyphs">HERON</text>
    <text class="brand-tagline" x="192" y="166" font-size="41" textLength="280" lengthAdjust="spacingAndGlyphs">COFFEE ROASTERS</text>
    <rect class="label__artwork" x="192" y="186" width="278" height="295" fill="url(#kraft-cup)" role="img" aria-label="Engraved illustration of a steaming coffee cup with roasted beans"/>
    <rect class="overprint-area--yellow" x="43" y="499" width="217" height="61"/>
    <text class="blend-name blend-name--yellow" x="278" y="533" font-size="42" textLength="194" lengthAdjust="spacingAndGlyphs">ITALIAN ROAST</text>
    <text class="web-address" x="278" y="559" font-size="11.5" textLength="190" lengthAdjust="spacingAndGlyphs">www.SilverHeronRoasters.example</text>
  </svg>

  <!-- Label option two: emblem artwork -->
  <svg class="label label--gem" viewBox="0 0 508 581" aria-label="Silver Heron Coffee Roasters label, Italian Roast">
    <defs>
      <linearGradient id="kraft-gem" x1="0" y1="0" x2="1" y2="1">
        <stop offset="0" class="kraft-start"/>
        <stop offset="0.6" class="kraft-start"/>
        <stop offset="1" class="kraft-end"/>
      </linearGradient>
    </defs>
    <rect class="label__bg" width="508" height="581"/>
    <text class="brand-vertical" transform="translate(169 481) rotate(-90)" font-size="172" textLength="445" lengthAdjust="spacingAndGlyphs">SILVER</text>
    <text class="brand-name" x="194" y="126" font-size="122" textLength="279" lengthAdjust="spacingAndGlyphs">HERON</text>
    <text class="brand-tagline brand-tagline--heavy" x="194" y="225" font-size="116" textLength="270" lengthAdjust="spacingAndGlyphs">COFFEE</text>
    <text class="brand-tagline brand-tagline--heavy" x="194" y="289" font-size="80" textLength="270" lengthAdjust="spacingAndGlyphs">ROASTERS</text>
    <rect class="label__artwork" x="191" y="324" width="276" height="157" fill="url(#kraft-gem)" role="img" aria-label="Line-drawn faceted emblem on kraft paper"/>
    <rect class="overprint-area--magenta" x="43" y="500" width="189" height="60"/>
    <text class="blend-name blend-name--magenta" x="246" y="539" font-size="48" textLength="218" lengthAdjust="spacingAndGlyphs">ITALIAN ROAST</text>
    <text class="web-address" x="246" y="560" font-size="12.5" textLength="218" lengthAdjust="spacingAndGlyphs">www.SilverHeronRoasters.example</text>
  </svg>

</main>
</body>
</html>
```